need corporate, modern business card created for Consulting Company

I need a slick business card using elements from my website, as well as, integrating my pixelharbor-created logo (see files).

The business card needs to be:
1. Corporate and modern
2. Clean and professional

I've included a PSD with the logo/icon that you can use to create it. Feel free to try a metallic finish on the logo, make it bigger/small, underlay it. Whatever you need to do to make my card stand out.

Try a black background, or white background or gray.

The idea is for my card to be memorable as well as professional and corporate.

Target Market(s)

Corporate business in the US and Canada.

Industry/Entity Type

Business

Contact Information for Business Card

Business Leveraging Technology
Malcolm Tudd, Senior Partner
office: 1 877 555 0143
mobile: 1 519 555 0172
website: http://www.vextorial.com

Requirements
Must have
• Card-related information
• corporate, yet modern
• clean and professional
• incorporate the icon only
• must have an editable form when complete!
Nice to have
• metallic icon might be cool
• try it with white or black

```html
<!DOCTYPE html>
<html lang="en">
<head>
<meta charset="utf-8">
<title>Vextorial Business Card</title>
<link href="https://fonts.googleapis.com/css2?family=Comfortaa:wght@500;700&family=Oswald:wght@400;500&display=swap" rel="stylesheet">
<style>
  :root {
    --stage: #0b0b0c;
    --card: #18191b;
    --card-edge: #232427;
    --ink-white: #f2f3f5;
    --ink-blue: #3f78cf;
    --ink-blue-soft: #6f9ad8;
    --rule-blue: #5b8fd8;
    --faint: #2a2c30;
  }
  * { margin: 0; padding: 0; box-sizing: border-box; }
  html, body {
    width: 1200px; height: 871px; overflow: hidden;
    background: var(--stage);
  }
  .stage {
    position: relative; width: 1200px; height: 871px;
    display: flex; flex-direction: column; align-items: center; justify-content: center;
    gap: 40px;
  }
  .card {
    position: relative; width: 630px; height: 360px;
    background: var(--card);
    border: 1px solid var(--card-edge);
    border-radius: 4px;
    overflow: hidden;
  }

  /* Back */
  .card-back .back-mark {
    position: absolute; inset: 0;
    display: flex; align-items: center; justify-content: center;
    font-family: "Comfortaa", sans-serif; font-weight: 700;
    font-size: 64px; color: var(--faint); letter-spacing: 1px;
  }

  /* Front */
  .accent-rule {
    position: absolute; left: 70px; top: 0;
    width: 5px; height: 180px;
    background: var(--rule-blue);
    transform: skewX(-10deg); transform-origin: top;
  }
  .identity { position: absolute; left: 92px; top: 44px; }
  .identity .name {
    font-family: "Comfortaa", sans-serif; font-weight: 500;
    font-size: 28px; color: var(--ink-white); letter-spacing: 0.5px;
  }
  .identity .role {
    margin-top: 4px;
    font-family: "Oswald", sans-serif; font-weight: 400;
    font-size: 12px; color: var(--ink-blue-soft); letter-spacing: 2px;
  }
  .brand {
    position: absolute; right: 40px; top: 40px;
    display: flex; align-items: center; gap: 12px;
  }
  .brand .brand-square { width: 26px; height: 26px; background: var(--ink-blue); border-radius: 3px; }
  .brand .brand-name {
    font-family: "Comfortaa", sans-serif; font-weight: 700;
    font-size: 34px; color: var(--ink-blue); letter-spacing: 1px;
  }
  .contacts {
    position: absolute; left: 40px; top: 230px;
    list-style: none;
    font-family: "Oswald", sans-serif; font-weight: 400;
    font-size: 17px; color: var(--ink-white); letter-spacing: 2px;
  }
  .contacts li { display: flex; align-items: center; gap: 14px; height: 29px; }
  .contacts svg { width: 18px; height: 16px; fill: var(--ink-blue-soft); }
  .web {
    position: absolute; right: 40px; bottom: 40px;
    display: flex; align-items: center; gap: 12px;
    font-family: "Oswald", sans-serif; font-weight: 500;
    font-size: 18px; color: var(--ink-blue); letter-spacing: 3px;
  }
  .web svg { width: 22px; height: 22px; }
</style>
</head>
<body>
<main class="stage">
  <section class="card card-back" aria-label="Card back">
    <div class="back-mark">vextorial</div>
  </section>

  <section class="card card-front" aria-label="Card front">
    <div class="accent-rule"></div>
    <div class="identity">
      <div class="name">Malcolm Tudd</div>
      <div class="role">Senior Partner</div>
    </div>
    <div class="brand">
      <span class="brand-square"></span>
      <span class="brand-name">vextorial</span>
    </div>
    <ul class="contacts">
      <li>
        <svg viewBox="0 0 18 16" aria-hidden="true"><path d="M2 5c0-2 3-3 7-3s7 1 7 3v1h-3V5H5v1H2z"/><rect x="4" y="7" width="10" height="7" rx="1"/></svg>
        1 877 555 0143
      </li>
      <li>
        <svg viewBox="0 0 18 16" aria-hidden="true"><path d="M5 0h8v16H5z M6.5 1.5v11h5v-11z"/></svg>
        1 519 555 0172
      </li>
      <li>
        <svg viewBox="0 0 18 16" aria-hidden="true"><path d="M1 3h16v11H1z M2 4l7 5 7-5v-.2H2z"/></svg>
        info@vextorial.com
      </li>
    </ul>
    <div class="web">
      <svg viewBox="0 0 22 22" aria-hidden="true">
        <circle cx="11" cy="11" r="10" fill="var(--ink-blue)"/>
        <path d="M5 7c2 0 3 1 3 3s2 2 2 4-1 3-2 4M14 4c-1 2 0 3 2 3s2 2 3 3" stroke="var(--card)" stroke-width="1.6" fill="none"/>
      </svg>
      www.vextorial.com
    </div>
  </section>
</main>
</body>
</html>
```